Cardinal Lino Barreda Conferencia

We need a postcard 5 x 7 inches to promote a visit in our Catholic parish, from Cardinal Lino Barreda of El Salvador. We want a Catholic content/background, and a nice picture of the Cardinal, which you can find in searchly. Cardinal will be giving Mass and will be giving a conference talk after the Mass. He will give Mass at 7pm at Saint Brendan of Meadowfield Catholic Church, 51270 Quill Orchard Pkwy, Sterling, VA 20164, and then he will be giving a talk afterwards at Vellmore Hall, which is a hall in the parish. Please put the following in Spanish. "Misa 7pm," "Conferencia 7:45pm (en Vellmore Hall)" The conference title should be "Familia, Iglesia doméstica y transmisora de la fe" And also add that there will be refreshments after the talk at "Café y Pan Dulce 9pm" The date is "Jueves, Agosto 17, 2023"

```html
<!DOCTYPE html>
<html lang="es">
<head>
<meta charset="utf-8">
<title>Cardenal Lino Barreda – Conferencia</title>
<link href="https://fonts.googleapis.com/css2?family=Oswald:wght@700&family=Titillium+Web:wght@400;600;700&display=swap" rel="stylesheet">
<style>
  :root{
    --navy:#1f3f73;
    --navy-dark:#183462;
    --yellow:#f7d31a;
    --ink:#2f3136;
    --panel-top:#ebebeb;
    --panel-bottom:#f7f7f7;
    --white:#ffffff;
  }
  *{margin:0;padding:0;box-sizing:border-box}
  html,body{width:1200px;height:904px;overflow:hidden;background:var(--white)}
  .postcard{position:relative;width:1200px;height:904px;overflow:hidden;font-family:"Titillium Web",sans-serif;background:var(--white)}
  .layer{position:absolute;inset:0}
  .panel{background:linear-gradient(180deg,var(--panel-top) 0%,var(--panel-bottom) 65%);clip-path:polygon(0 0,539px 0,735px 444px,528px 904px,0 904px)}
  .panel-lower{position:absolute;left:0;top:596px;width:760px;height:308px;background:var(--white);clip-path:polygon(0 0,640px 0,528px 308px,0 308px)}
  .speaker-faded{position:absolute;left:395px;top:125px;width:300px;height:471px;
    background:radial-gradient(ellipse at 55% 40%,#d2d2d2 0%,#e2e2e2 45%,rgba(235,235,235,0) 75%);
    clip-path:polygon(0 0,144px 0,340px 471px,0 471px)}
  .speaker-photo{background:linear-gradient(160deg,#3a2424 0%,#5b2e27 35%,#c8401f 65%,#e8552a 100%);
    clip-path:polygon(670px 0,1200px 0,1200px 904px,692px 904px,745px 444px)}
  .chevron{position:absolute;inset:0}
  .title{position:absolute;left:50px;top:40px;font-family:"Oswald",sans-serif;font-weight:700;font-size:62px;line-height:72px;text-transform:uppercase;letter-spacing:-.3px}
  .title .accent{color:var(--navy)}
  .title .dark{color:var(--ink)}
  .schedule{position:absolute;left:0;top:358px;width:590px;height:127px;background:var(--navy);clip-path:polygon(0 0,562px 0,590px 63px,562px 127px,0 127px);
    padding:14px 0 0 50px;color:var(--white);font-weight:700;font-size:35px;line-height:45px}
  .schedule .time{color:var(--yellow)}
  .schedule .place{font-size:23px;font-weight:600;color:var(--white)}
  .date{position:absolute;left:50px;top:506px;display:flex;align-items:center;height:80px}
  .icon-circle{width:74px;height:74px;border-radius:50%;background:var(--navy);border:4px solid #d6d9e0;display:flex;align-items:center;justify-content:center;flex:none}
  .date .day{font-family:"Oswald",sans-serif;font-weight:700;font-size:76px;color:var(--navy);margin-left:10px;line-height:1}
  .date .divider{width:2px;height:62px;background:var(--navy);margin:0 12px}
  .date .weekday{font-weight:700;font-size:27px;line-height:33px;color:var(--navy);text-transform:uppercase}
  .date .weekday span{display:block}
  .date .weekday .month{color:var(--ink)}
  .detail{position:absolute;left:50px;display:flex;align-items:center}
  .detail .text{margin-left:14px}
  .venue{top:606px}
  .venue .name{font-weight:700;font-size:24px;line-height:28px;color:var(--navy)}
  .venue .address{font-weight:600;font-size:20px;line-height:26px;color:#1c1c1c}
  .refreshments{top:700px}
  .refreshments .name{font-weight:700;font-size:27px;line-height:29px;color:var(--navy)}
  .refreshments .menu{font-weight:600;font-size:20px;line-height:23px;color:#1c1c1c}
  .refreshments .note{font-size:17px;line-height:21px;color:#333}
  .organizer{position:absolute;left:0;top:797px;width:700px;height:107px;background:var(--navy);clip-path:polygon(0 0,575px 0,528px 107px,0 107px);
    padding:12px 0 0 50px;color:var(--white);font-size:29px;line-height:38px;font-weight:600}
  .organizer .label{color:var(--yellow);font-weight:700}
  .holy-family{position:absolute;left:390px;top:689px;width:136px;height:195px;background:linear-gradient(160deg,#d49a3c 0%,#b7352a 55%,#7a2a24 100%)}
  .speaker-tag{position:absolute;left:770px;top:749px;width:430px;height:100px;background:var(--navy);clip-path:polygon(0 0,430px 0,430px 100px,58px 100px);
    text-align:right;padding:8px 50px 0 0}
  .speaker-tag .name{color:var(--yellow);font-size:32px;line-height:38px;font-weight:600}
  .speaker-tag .origin{color:var(--white);font-size:27px;line-height:32px}
  .phone{position:absolute;left:880px;top:849px;width:320px;height:52px;background:var(--yellow);clip-path:polygon(18px 0,320px 0,320px 52px,0 52px);
    display:flex;align-items:center;justify-content:flex-end;padding-right:48px;gap:10px;color:var(--navy-dark);font-weight:700;font-size:29px}
</style>
</head>
<body>
<div class="postcard">
  <div class="layer panel"></div>
  <div class="speaker-faded" role="img" aria-label="Faded black and white photo of the Cardinal speaking into a microphone"></div>
  <div class="panel-lower"></div>
  <div class="layer speaker-photo" role="img" aria-label="Photo of the Cardinal in red choir robes with zucchetto and biretta"></div>

  <svg class="chevron" width="1200" height="904" viewBox="0 0 1200 904" aria-hidden="true">
    <polygon points="539,0 670,0 745,444 735,444" fill="#1f3f73"/>
    <polygon points="735,444 745,444 692,904 528,904" fill="#1f3f73"/>
  </svg>

  <h1 class="title">
    <span class="accent">Familia, Iglesia</span><br>
    <span class="dark">Doméstica y</span><br>
    <span class="accent">Transmisora</span><br>
    <span class="dark">de la fe</span>
  </h1>

  <div class="schedule">
    <div>Misa <span class="time">7pm</span></div>
    <div>Conferencia <span class="time">7:45pm</span> <span class="place">(en Vellmore Hall)</span></div>
  </div>

  <div class="date">
    <div class="icon-circle">
      <svg width="36" height="36" viewBox="0 0 24 24" fill="none" stroke="#fff" stroke-width="2"><rect x="3" y="5" width="18" height="16" rx="2"/><path d="M3 10h18M8 3v4M16 3v4"/><path d="M7 14h2M11 14h2M15 14h2M7 17h2M11 17h2M15 17h2" stroke-width="1.6"/></svg>
    </div>
    <div class="day">17</div>
    <div class="divider"></div>
    <div class="weekday"><span>Jueves,</span><span class="month">Agosto 2023</span></div>
  </div>

  <div class="detail venue">
    <div class="icon-circle">
      <svg width="36" height="36" viewBox="0 0 24 24" fill="none" stroke="#fff" stroke-width="2"><path d="M12 21s-6-6.2-6-11a6 6 0 0 1 12 0c0 4.8-6 11-6 11z"/><circle cx="12" cy="10" r="2.3"/><path d="M5 20h14" stroke-width="1.6"/></svg>
    </div>
    <div class="text">
      <div class="name">Iglesia Católica Saint Brendan of Meadowfield</div>
      <div class="address">51270 Quill Orchard Pkwy, Sterling, VA 20164</div>
    </div>
  </div>

  <div class="detail refreshments">
    <div class="icon-circle">
      <svg width="38" height="38" viewBox="0 0 24 24" fill="#fff"><path d="M4 10h11v5a4 4 0 0 1-4 4H8a4 4 0 0 1-4-4z"/><path d="M15 11h2a2 2 0 0 1 0 4h-2" fill="none" stroke="#fff" stroke-width="1.6"/><path d="M7 4c1 1-1 2 0 3M10 4c1 1-1 2 0 3" fill="none" stroke="#fff" stroke-width="1.3"/><rect x="3" y="20" width="15" height="1.6"/></svg>
    </div>
    <div class="text">
      <div class="name">Refrigerio</div>
      <div class="menu">Café y Pan Dulce 9pm</div>
      <div class="note">(después de la conferencia)</div>
    </div>
  </div>

  <div class="organizer">
    <div class="label">Organiza:</div>
    <div>Hogares de Valle Sereno</div>
  </div>

  <div class="holy-family" role="img" aria-label="Icon painting of the Holy Family"></div>

  <div class="speaker-tag">
    <div class="name">Cardenal Lino Barreda</div>
    <div class="origin">de El Salvador</div>
  </div>

  <div class="phone">
    <span>571-555-0148</span>
    <svg width="28" height="28" viewBox="0 0 24 24"><circle cx="12" cy="12" r="11" fill="#1f3f73"/><path d="M8.5 6.5l2 2.3-1.2 1.6a7 7 0 0 0 4.3 4.3l1.6-1.2 2.3 2-1.3 1.8c-4.8-.3-8.6-4.1-8.9-8.9z" fill="#f7d31a"/></svg>
  </div>
</div>
</body>
</html>
```